WP website design for Brenwick

We need a wordpress design for an auction company. The winning design will incorporate a professional color scheme with company logo in a clean, image driven layout. The design needs to consider that this will be developed on a responsive theme. Colors are those that will highlight the logo.

Industry/Entity Type

It Company

Font styles to use
Serif
Sans Serif

Colors

Designer to choose colors to be used in the design.

Requirements
Must have
• Navigation: 1) Home 2) Auctions 3) Services 4) Real Estate 5 ) Previous Auctions 6) About Us 7) Contact Us

Sites referenced that client likes: https://www.gatherpledge.example/ and http://www.quillonbidhouse.example/ as examples of image rich sites. There will be large slideshow element and 4 calls to action (with any stock images suitable) 1) Real Estate 2) Auctions 3) Liquidations 4) Appraisals

Content will also include text (below) and auctions as seen at http://www.quillonbidhouse.example/ below the slideshow or as in the attached image.

Footer will have contact info, social icons (FB, Twitter, YT, RSS) and news posts widget

Colors will be that of the logo and any others to highlight/compliment the design.

Nice to have
• Use of dropdown menu styling

```html
<!DOCTYPE html>
<html lang="en">
<head>
<meta charset="utf-8">
<title>Brenwick Auctions</title>
<link href="https://fonts.googleapis.com/css2?family=Noto+Serif:wght@400;700&family=Roboto:wght@400;500;700&family=Quicksand:wght@500;700&display=swap" rel="stylesheet">
<style>
:root{
  --navy:#14307a;
  --navy-dark:#0d2160;
  --ink:#222;
  --red:#c41a1a;
  --maroon:#8e0f1f;
  --paper:#ececec;
  --white:#fff;
  --footer:#1f2424;
  --line:#d6d6d6;
}
*{box-sizing:border-box;margin:0;padding:0}
html,body{width:987px;height:1200px;overflow:hidden}
body{position:relative;background:var(--paper);font-family:"Roboto",Arial,sans-serif;color:var(--ink)}
.abs{position:absolute}

/* header */
.brand{left:82px;top:15px;width:275px;height:74px;display:flex;align-items:center;gap:10px}
.brand-mark{width:16px;height:16px;background:var(--navy)}
.brand-name{font-family:"Noto Serif",Georgia,serif;font-weight:700;font-size:24px;color:var(--navy);letter-spacing:.5px}
.contact-phone{left:750px;top:11px;display:flex;gap:6px}
.contact-label{font-family:"Quicksand",sans-serif;font-size:12px;color:#666;line-height:14px}
.contact-number{font-family:"Quicksand",sans-serif;font-weight:700;font-size:16px;color:var(--navy);line-height:20px}
.contact-address{left:754px;top:62px;display:flex;gap:8px;font-family:"Quicksand",sans-serif;font-weight:500;font-size:12px;color:#555;line-height:18px}

/* nav */
.nav{left:0;top:105px;width:987px;height:35px;background:var(--navy)}
.nav a{position:absolute;top:0;height:35px;line-height:35px;font-size:10.5px;font-weight:700;color:var(--white);text-decoration:none;letter-spacing:.2px}
.nav a.active{background:#111;padding:0 12px}
.search{left:750px;top:114px;width:154px;height:19px;background:var(--white);font-size:10px;color:#888;padding:3px 6px}
.search svg{position:absolute;right:4px;top:3px}

/* hero */
.hero{left:82px;top:153px;width:822px;height:336px;background:var(--white);box-shadow:0 0 3px rgba(0,0,0,.2)}
.hero-image{left:4px;top:3px;width:814px;height:329px;background:linear-gradient(180deg,#5a8ed8 0%,#8fb6ea 40%,#b7b0a2 62%,#4f7a3a 85%,#6b8f4a 100%)}
.dropdown{left:120px;top:146px;width:114px;height:92px;background:#1d2a36;border-radius:3px;padding:3px;z-index:2}
.dropdown::before{content:"";position:absolute;left:57px;top:-6px;border:6px solid transparent;border-top:0;border-bottom-color:#1d2a36}
.dropdown a{display:block;height:28px;line-height:26px;font-family:"Noto Serif",Georgia,serif;font-size:10.5px;color:var(--white);text-decoration:none;padding-left:8px;border-bottom:1px solid #3b4a58}
.dropdown a:last-child{border:0}
.dropdown a.current{background:#0f3a73}
.signup{left:617px;top:230px;width:278px;height:235px;background:rgba(30,30,30,.93)}
.signup h2{position:absolute;left:23px;top:22px;font-family:"Noto Serif",Georgia,serif;font-weight:400;font-size:20px;color:var(--white)}
.field{position:absolute;left:23px;width:224px;height:29px;border-radius:15px;background:#eee;font-size:10.5px;color:#444;line-height:29px;padding-left:14px}
.subscribe{position:absolute;left:122px;top:158px;width:124px;height:33px;border-radius:10px;background:var(--navy);border:1px solid #6e88c8;color:var(--white);font-size:14px;font-weight:500;text-align:center;line-height:31px}

/* panels */
.panel{background:var(--white);box-shadow:0 0 2px rgba(0,0,0,.15)}
.panel-head{height:34px;font-family:"Noto Serif",Georgia,serif;font-size:17px;color:var(--white);padding-left:19px;line-height:34px;letter-spacing:.5px}
.head-blue{background:linear-gradient(#2a4ca4,#0f2a7a);border:1px solid #4a63a4}
.head-black{background:linear-gradient(#444,#0c0c0c);height:32px;line-height:32px}
.main{left:82px;top:517px;width:550px;height:552px}

.lot{position:absolute;left:15px;width:510px;height:140px}
.lot-photo{position:absolute;left:0;top:0;width:91px;height:67px;background:linear-gradient(160deg,#6f8b5c,#b9bcc2 45%,#8b8f94 70%,#5c6b4a);border:1px solid #ddd}
.lot-links{position:absolute;left:0;top:84px;font-size:10.5px;font-weight:500;color:var(--navy)}
.lot-links div{display:flex;align-items:flex-start;gap:6px;margin-bottom:7px;line-height:13px}
.lot-title{position:absolute;left:109px;top:0;font-size:12.5px;font-weight:700;color:var(--red);letter-spacing:.6px}
.lot-type{position:absolute;left:111px;top:21px;font-size:11.5px;font-weight:500;letter-spacing:.8px}
.lot-meta{position:absolute;left:111px;font-size:10.3px}
.lot-meta b{font-weight:700}
.lot-desc{position:absolute;left:109px;top:78px;width:403px;font-size:9.9px;line-height:12px;text-align:justify;color:#333}
.rule{position:absolute;left:15px;width:508px;border-top:1px dashed #bbb}

.side-feature{left:669px;top:517px;width:236px;height:162px}
.side-link{position:absolute;left:20px;top:41px;font-size:10.5px;font-weight:500;color:var(--red);text-decoration:underline;letter-spacing:.5px}
.side-photo{position:absolute;left:19px;top:64px;width:89px;height:56px;background:linear-gradient(120deg,#c9c2b4,#8b857a 50%,#d8d2c4)}
.side-date{position:absolute;left:121px;top:64px;font-size:9.8px;font-weight:700;line-height:12px}
.side-place{position:absolute;left:121px;top:101px;font-size:9.8px;line-height:12px}
.read-more{position:absolute;left:167px;top:134px;width:59px;height:19px;background:var(--maroon);border-radius:4px;color:var(--white);font-size:9.5px;font-style:italic;text-align:center;line-height:19px}

.video{left:669px;top:700px;width:235px;height:183px;background:radial-gradient(ellipse at 50% 45%,#3a3a3a,#080808 75%)}
.play{left:93px;top:62px;width:48px;height:37px;background:#1a1a1a;border:1px solid #333}
.controls{left:5px;top:161px;width:225px;height:17px;background:#222;border:1px solid #444;font-size:7px;color:#ccc}

.testimonials{left:669px;top:907px;width:236px;height:162px}
.quote{position:absolute;left:17px;top:46px;width:208px;font-size:10.5px;line-height:15px;color:#333}
.quote-mark{font-family:"Noto Serif",Georgia,serif;font-size:16px;color:#aaa;line-height:0}

/* footer */
.footer{left:0;top:1096px;width:987px;height:104px;background:var(--footer);border-top:4px solid var(--navy)}
.footer-links{left:90px;top:27px;font-size:10.5px;color:var(--white)}
.footer-links span{margin:0 6px;color:#aaa}
.copyright{left:91px;top:52px;font-size:10.5px;color:var(--white)}
.badge{position:absolute;top:35px;height:34px;background:#9aa0a0;opacity:.55}
</style>
</head>
<body>

<header>
  <div class="abs brand">
    <span class="brand-mark"></span>
    <span class="brand-name">BRENWICK AUCTIONS</span>
  </div>
  <div class="abs contact-phone">
    <svg width="30" height="30" viewBox="0 0 30 30" fill="none" stroke="#3a3a3a" stroke-width="2.2"><path d="M6 6c-3 3-2 9 4 15s12 7 15 4l-4-5-4 2c-2-1-6-5-7-7l2-4z"/><path d="M17 4a9 9 0 0 1 9 9M17 9a4 4 0 0 1 4 4"/></svg>
    <div>
      <div class="contact-label">TOLL FREE NO</div>
      <div class="contact-number">1800-555-0142</div>
    </div>
  </div>
  <div class="abs contact-address">
    <svg width="24" height="28" viewBox="0 0 24 28" fill="none" stroke="#3a3a3a" stroke-width="2.2"><path d="M12 26s9-9 9-15a9 9 0 0 0-18 0c0 6 9 15 9 15z"/><circle cx="12" cy="11" r="3.5"/></svg>
    <div>214 Meadowlark Lane,<br>Corvale, PA 19002</div>
  </div>
</header>

<nav class="abs nav">
  <a style="left:90px">HOME</a>
  <a class="active" style="left:137px">AUCTIONS</a>
  <a style="left:229px">SERVICES</a>
  <a style="left:308px">REAL ESTATE</a>
  <a style="left:404px">PREVIOUS AUCTIONS</a>
  <a style="left:540px">ABOUT US</a>
  <a style="left:620px">CONTACT US</a>
</nav>
<div class="abs search">Search
  <svg width="14" height="12" viewBox="0 0 14 12" fill="none" stroke="#14307a" stroke-width="2"><path d="M0 6h12M7 1l5 5-5 5"/></svg>
</div>

<section class="abs hero">
  <div class="abs hero-image" role="img" aria-label="Photo of a large suburban house with stone trim and a landscaped front garden under a blue sky"></div>
  <form class="abs signup" style="left:535px;top:77px">
    <h2>Email sign-up form</h2>
    <div class="field" style="top:80px">First Name</div>
    <div class="field" style="top:125px">Email Address</div>
    <div class="subscribe">Subscribe Now</div>
  </form>
</section>

<div class="abs dropdown">
  <a class="current">» Current Auctions</a>
  <a>» Past Auctions</a>
  <a>» Online Auctions</a>
</div>

<main class="abs panel main">
  <h2 class="panel-head head-blue">Featured Auctions</h2>

  <article class="lot" style="top:56px">
    <div class="lot-photo" role="img" aria-label="Photo of a silver minivan parked on grass"></div>
    <div class="lot-links">
      <div><svg width="21" height="10"><rect width="9" height="9" fill="#111"/><path d="M11 1.5h10M11 4.5h10M11 7.5h10" stroke="#111" stroke-width="1.6"/></svg>Details</div>
      <div><svg width="21" height="20" fill="none" stroke="#111" stroke-width="1.6"><rect x="2" y="2" width="13" height="11"/><rect x="6" y="6" width="13" height="11" fill="#fff"/><circle cx="12" cy="11" r="2.5"/></svg>Photo<br>Galleries</div>
    </div>
    <h3 class="lot-title">Shop Equipment/tools <span style="font-weight:400">*</span> Pork Processing Items</h3>
    <div class="lot-type">LIVE ON-SITE AUCTION</div>
    <div class="lot-meta" style="top:42px"><b>Begins:</b>&nbsp; Saturday, March 16, 2013 at 10:00 AM EDT</div>
    <div class="lot-meta" style="top:58px"><b>Location:</b>&nbsp; 880 Hollis Road Ashby, KY 40117</div>
    <p class="lot-desc">Kestrel BS3F High Lift, simply dummy text of the printing and typesetting industry simply dummy text of the printing and typesetting industry 600 Series Harrow tractor w/Tallis Loader, Dune buggy, 1207 HT Cutditioner: SHOP &amp; MISCELLANIOUS &amp; PORK PROCESSING ITEMS.</p>
  </article>
  <div class="rule" style="top:199px"></div>

  <article class="lot" style="top:221px">
    <div class="lot-photo" role="img" aria-label="Photo of a silver minivan parked on grass"></div>
    <div class="lot-links">
      <div><svg width="21" height="10"><rect width="9" height="9" fill="#111"/><path d="M11 1.5h10M11 4.5h10M11 7.5h10" stroke="#111" stroke-width="1.6"/></svg>Details</div>
      <div><svg width="21" height="20" fill="none" stroke="#111" stroke-width="1.6"><rect x="2" y="2" width="13" height="11"/><rect x="6" y="6" width="13" height="11" fill="#fff"/><circle cx="12" cy="11" r="2.5"/></svg>Photo<br>Galleries</div>
    </div>
    <h3 class="lot-title">Shop Equipment/tools <span style="font-weight:400">*</span> Pork Processing Items</h3>
    <div class="lot-type">LIVE ON-SITE AUCTION</div>
    <div class="lot-meta" style="top:42px"><b>Begins:</b>&nbsp; Saturday, March 16, 2013 at 10:00 AM EDT</div>
    <div class="lot-meta" style="top:58px"><b>Location:</b>&nbsp; 880 Hollis Road Ashby, KY 40117</div>
    <p class="lot-desc">Kestrel BS3F High Lift, simply dummy text of the printing and typesetting industry simply dummy text of the printing and typesetting industry 600 Series Harrow tractor w/Tallis Loader, Dune buggy, 1207 HT Cutditioner: SHOP &amp; MISCELLANIOUS &amp; PORK PROCESSING ITEMS.</p>
  </article>
  <div class="rule" style="top:364px"></div>

  <article class="lot" style="top:389px">
    <div class="lot-photo" role="img" aria-label="Photo of a silver minivan parked on grass"></div>
    <div class="lot-links">
      <div><svg width="21" height="10"><rect width="9" height="9" fill="#111"/><path d="M11 1.5h10M11 4.5h10M11 7.5h10" stroke="#111" stroke-width="1.6"/></svg>Details</div>
      <div><svg width="21" height="20" fill="none" stroke="#111" stroke-width="1.6"><rect x="2" y="2" width="13" height="11"/><rect x="6" y="6" width="13" height="11" fill="#fff"/><circle cx="12" cy="11" r="2.5"/></svg>Photo<br>Galleries</div>
    </div>
    <h3 class="lot-title">Shop Equipment/tools <span style="font-weight:400">*</span> Pork Processing Items</h3>
    <div class="lot-type">LIVE ON-SITE AUCTION</div>
    <div class="lot-meta" style="top:42px"><b>Begins:</b>&nbsp; Saturday, March 16, 2013 at 10:00 AM EDT</div>
    <div class="lot-meta" style="top:58px"><b>Location:</b>&nbsp; 880 Hollis Road Ashby, KY 40117</div>
    <p class="lot-desc">Kestrel BS3F High Lift, simply dummy text of the printing and typesetting industry simply dummy text of the printing and typesetting industry 600 Series Harrow tractor w/Tallis Loader, Dune buggy, 1207 HT Cutditioner: SHOP &amp; MISCELLANIOUS &amp; PORK PROCESSING ITEMS.</p>
  </article>
</main>

<aside>
  <section class="abs panel side-feature">
    <h2 class="panel-head head-black">Featured Auctions</h2>
    <a class="side-link">TRACTOR * HI LIFT * MACHINERY</a>
    <div class="side-photo" role="img" aria-label="Photo of industrial printing machinery in a workshop"></div>
    <div class="side-date">Saturday March 16,<br>2013 at 10:00 AM EDT</div>
    <div class="side-place">Hollis Road<br>Ashby, KY 40117</div>
    <div class="read-more">read more</div>
  </section>

  <section class="abs video" role="img" aria-label="Company video player">
    <div class="abs play">
      <svg width="48" height="37"><path d="M19 9l13 9.5L19 28z" fill="#ddd"/></svg>
    </div>
    <div class="abs controls">
      <svg width="225" height="15">
        <path d="M5 4l6 3.5L5 11z" fill="#eee"/>
        <text x="27" y="10" fill="#ccc" font-size="7" font-family="Roboto,sans-serif">00:00</text>
        <rect x="52" y="6" width="97" height="3" fill="#777"/>
        <text x="154" y="10" fill="#ccc" font-size="7" font-family="Roboto,sans-serif">00:00</text>
        <path d="M184 6h3l3-2v7l-3-2h-3z" fill="#ccc"/>
        <path d="M193 10v-1M195 10v-2M197 10v-3M199 10v-4M201 10v-5" stroke="#ccc"/>
        <rect x="211" y="4" width="7" height="7" fill="none" stroke="#ccc"/>
      </svg>
    </div>
  </section>

  <section class="abs panel testimonials">
    <h2 class="panel-head head-black">Clients Testimonials</h2>
    <p class="quote"><span class="quote-mark">“</span> simply dummy text of the printing and typesetting industry. Lorem Ipsum has been the industry's standard dummy text ever since the 1500s, when an unknown printer took a galley of type. <span class="quote-mark">”</span></p>
  </section>
</aside>

<footer class="abs footer">
  <div class="abs footer-links">Home<span>|</span>Auctions<span>|</span>Online Auctions<span>|</span>About Us<span>|</span>Contact Us</div>
  <div class="abs copyright">Copyright (C) Brenwick_AuctionServices.example 2013.&nbsp; All Rights Reserved</div>
  <div class="badge" style="left:543px;width:46px"></div>
  <div class="badge" style="left:603px;width:62px;border-radius:50%"></div>
  <div class="badge" style="left:671px;width:50px"></div>
  <div class="badge" style="left:741px;width:46px"></div>
  <div class="badge" style="left:808px;width:28px"></div>
  <div class="badge" style="left:865px;width:34px"></div>
</footer>

</body>
</html>
```